Larkvale Gastroenterology business cards, stationary and envelopes
Larkvale Gastroenterology business cards, stationary and envelopes - Medical
Creative Brief
Simple
Dorian Velmoretti, M.D.
Gastroenterology And Liver Disease (and under it) Clinical Nutrition
17 West 63rd, Suite 4C New York, NY 10342
dorianvelm@quillbox.net
www.pinwardclinic.com
Would like professional, stylish business card (front and back), envelopes and full stationary package required. Front card should be white bacground. please see my website www.pinwardclinic.com
I am open to ideas, possibly just the website and logo

```html
<!DOCTYPE html>
<html lang="en">
<head>
<meta charset="utf-8">
<title>Larkvale Gastroenterology Stationery</title>
<link rel="stylesheet" href="https://fonts.googleapis.com/css2?family=Cinzel:wght@600&family=Lato:wght@400;700&display=swap">
<style>
  :root {
    --board: #3d3d3d;
    --board-light: #5a5a5a;
    --paper: #ffffff;
    --ink: #111111;
    --muted: #777777;
    --faint: #e6e6e6;
    --label: #bdbdbd;
  }
  * { box-sizing: border-box; margin: 0; padding: 0; }
  html, body { width: 1200px; height: 438px; overflow: hidden; }
  body {
    position: relative;
    background: radial-gradient(ellipse at 50% 40%, var(--board-light), var(--board) 75%);
    font-family: "Lato", Arial, sans-serif;
    color: var(--ink);
  }
  .item { position: absolute; background: var(--paper); overflow: hidden; box-shadow: 0 3px 8px rgba(0,0,0,.45); }
  .label { position: absolute; font-size: 7px; color: var(--label); text-align: center; letter-spacing: .3px; }

  .brand { display: flex; align-items: center; gap: 4px; }
  .brand-dot { border-radius: 50%; background: var(--ink); flex: none; }
  .brand-name { font-family: "Cinzel", Georgia, serif; font-weight: 600; line-height: 1.05; color: var(--ink); }
  .brand.inverse .brand-dot { background: var(--paper); }
  .brand.inverse .brand-name { color: var(--paper); }

  .faint-mark { position: absolute; border-radius: 50%; background: var(--faint); display: flex; align-items: center; justify-content: center; text-align: center; font-family: "Cinzel", Georgia, serif; font-weight: 600; color: #d3d3d3; }
  .swoosh { position: absolute; left: 0; bottom: 0; width: 100%; }

  /* business cards */
  .card { left: 20px; width: 148px; }
  .card-front { top: 100px; height: 88px; }
  .card-back { top: 228px; height: 88px; }
  .card-dark { top: 352px; height: 66px; background: var(--ink); }
  .card-front .brand { position: absolute; left: 8px; top: 8px; }
  .card-details { position: absolute; left: 8px; top: 34px; font-size: 4.6px; line-height: 1.45; color: var(--muted); }
  .card-details strong { color: var(--ink); font-size: 5.4px; }
  .card-contact { position: absolute; right: 8px; top: 34px; font-size: 4.6px; line-height: 1.45; color: var(--muted); text-align: right; }
  .card-dark .brand { position: absolute; left: 28px; top: 22px; }

  /* letterheads */
  .letter { top: 24px; width: 258px; height: 372px; }
  .letter-one { left: 212px; }
  .letter-two { left: 507px; }
  .letter .brand { position: absolute; left: 14px; top: 14px; }
  .letter-contact { position: absolute; right: 14px; top: 16px; font-size: 4.4px; line-height: 1.5; color: var(--muted); text-align: right; }
  .letter .faint-mark { left: 44px; top: 110px; width: 170px; height: 170px; font-size: 11px; }
  .letter-foot { position: absolute; left: 0; right: 0; bottom: 14px; font-size: 4.2px; color: var(--muted); text-align: center; }

  /* envelopes */
  .env { left: 864px; width: 316px; }
  .env-grey { top: 24px; height: 92px; }
  .env-dark { top: 124px; height: 88px; }
  .env-plain { top: 220px; height: 86px; }
  .env-mark { top: 314px; height: 84px; }
  .env-grey .flap { position: absolute; inset: 0 0 40% 0; background: linear-gradient(#8e8e8e, #d8d8d8); clip-path: polygon(0 0, 100% 0, 100% 55%, 50% 100%, 0 55%); }
  .env-grey .brand { position: absolute; left: 134px; top: 16px; }
  .env-dark .band { position: absolute; left: 0; right: 0; top: 0; height: 52px; background: var(--ink); clip-path: polygon(0 0, 100% 0, 100% 60%, 50% 100%, 0 60%); }
  .env-dark .brand { position: absolute; left: 132px; top: 12px; }
  .env-web { position: absolute; left: 0; right: 0; top: 56px; font-size: 4.6px; color: var(--muted); text-align: center; }
  .env-plain .brand { position: absolute; left: 10px; top: 10px; }
  .env-plain .faint-mark { right: 14px; top: 4px; width: 78px; height: 78px; font-size: 6px; }
  .env-mark .faint-mark { left: 8px; top: 4px; width: 76px; height: 76px; font-size: 6px; }
</style>
</head>
<body>

  <!-- business cards -->
  <section class="item card card-front">
    <div class="brand"><span class="brand-dot" style="width:14px;height:14px"></span><span class="brand-name" style="font-size:6.5px">Larkvale<br>Gastroenterology</span></div>
    <div class="card-details"><strong>Dorian Velmoretti, M.D.</strong><br>Gastroenterology and Liver Disease<br>Clinical Nutrition</div>
    <div class="card-contact">17 West 63rd, Suite 4C<br>New York, NY 10342<br>212-555-0148<br>dorianvelm@quillbox.net</div>
    <svg class="swoosh" viewBox="0 0 148 14" height="14" preserveAspectRatio="none"><path d="M0 14 L0 8 Q74 -2 148 8 L148 14 Z" fill="#111"/></svg>
  </section>
  <p class="label" style="left:20px;top:192px;width:148px">Business Card Front</p>

  <section class="item card card-back">
    <div class="faint-mark" style="left:44px;top:10px;width:60px;height:60px;font-size:5px">Larkvale</div>
    <svg class="swoosh" viewBox="0 0 148 14" height="14" preserveAspectRatio="none"><path d="M0 14 L0 8 Q74 -2 148 8 L148 14 Z" fill="#111"/></svg>
  </section>
  <p class="label" style="left:20px;top:320px;width:148px">Business Card Back</p>

  <section class="item card card-dark">
    <div class="brand inverse"><span class="brand-dot" style="width:16px;height:16px"></span><span class="brand-name" style="font-size:7.5px">Larkvale<br>Gastroenterology</span></div>
  </section>
  <p class="label" style="left:20px;top:422px;width:148px">Business Card Alt</p>

  <!-- letterheads -->
  <section class="item letter letter-one">
    <div class="brand"><span class="brand-dot" style="width:16px;height:16px"></span><span class="brand-name" style="font-size:7.5px">Larkvale<br>Gastroenterology</span></div>
    <div class="letter-contact">17 West 63rd, Suite 4C<br>New York, NY 10342<br>212-555-0148<br>dorianvelm@quillbox.net</div>
    <div class="faint-mark" role="img" aria-label="Faint circular brand emblem">Larkvale</div>
    <p class="letter-foot">www.pinwardclinic.com</p>
    <svg class="swoosh" viewBox="0 0 258 12" height="12" preserveAspectRatio="none"><path d="M0 12 L0 7 Q129 -2 258 7 L258 12 Z" fill="#111"/></svg>
  </section>
  <p class="label" style="left:212px;top:404px;width:258px">Letterhead Page One</p>

  <section class="item letter letter-two">
    <div class="faint-mark" role="img" aria-label="Faint circular brand emblem">Larkvale</div>
    <p class="letter-foot">www.pinwardclinic.com</p>
    <svg class="swoosh" viewBox="0 0 258 12" height="12" preserveAspectRatio="none"><path d="M0 12 L0 7 Q129 -2 258 7 L258 12 Z" fill="#111"/></svg>
  </section>
  <p class="label" style="left:507px;top:404px;width:258px">Letterhead Page Two</p>

  <!-- envelopes -->
  <section class="item env env-grey">
    <div class="flap"></div>
    <div class="brand"><span class="brand-dot" style="width:14px;height:14px"></span></div>
  </section>

  <section class="item env env-dark">
    <div class="band"></div>
    <div class="brand inverse"><span class="brand-dot" style="width:10px;height:10px"></span><span class="brand-name" style="font-size:5.5px">Larkvale</span></div>
    <p class="env-web">www.pinwardclinic.com</p>
  </section>

  <section class="item env env-plain">
    <div class="brand"><span class="brand-dot" style="width:13px;height:13px"></span><span class="brand-name" style="font-size:6px">Larkvale<br>Gastroenterology</span></div>
    <div class="faint-mark" role="img" aria-label="Faint circular brand emblem">Larkvale</div>
  </section>

  <section class="item env env-mark">
    <div class="faint-mark" role="img" aria-label="Faint circular brand emblem">Larkvale</div>
  </section>
  <p class="label" style="left:864px;top:404px;width:316px">Envelopes Front And Back</p>

</body>
</html>
```